PowerPoint template for Law Firm

We Need a PowerPoint Template for a Law Firm in Switzerland. We are primarly consult in business law. We Need a template for PowerPoint to Show Information to our Clients (inheritence law, corporate law, legal structures etc.) The design should be contemporary, simple and clear. It should be in harmony with our website: www.trovanek.com Style: professional, structured and clearly arranged. Colors: Blue (R: 1, G: 61: B: 105), white. Font: Calibri Ratio: 16: 9 Esamples attached

```html
<!DOCTYPE html>
<html lang="en">
<head>
<meta charset="utf-8">
<title>Trovanek Lawyers – Presentation Template</title>
<link rel="stylesheet" href="https://fonts.googleapis.com/css2?family=Mulish:wght@400;600;700;800&display=swap">
<style>
  :root{
    --navy:#14427f;
    --deep:#0f3768;
    --blue:#1765b0;
    --bright:#1f7fcc;
    --sky:#4a97d6;
    --cyan:#2aa6e6;
    --grey:#e8e8ea;
    --white:#ffffff;
    --gold:#d3ad4f;
    --photo-a:#cfcfcf;
    --photo-b:#5d5d5d;
  }
  *{box-sizing:border-box;margin:0;padding:0}
  html,body{width:1200px;height:1116px;overflow:hidden;background:var(--white)}
  body{position:relative;font-family:"Mulish",sans-serif;color:var(--white)}
  .slide{position:absolute;width:360px;height:218px;overflow:hidden}
  .abs{position:absolute}
  .svg-fill{position:absolute;left:0;top:0;width:100%;height:100%}
  .body-text{font-size:3.7px;line-height:1.45;font-weight:400;text-align:justify}
  .photo{background:linear-gradient(135deg,var(--photo-a),#9a9a9a 55%,var(--photo-b))}
  .col-1{left:49px}.col-2{left:422px}.col-3{left:802px}
  .row-1{top:80px}.row-2{top:324px}.row-3{top:560px}.row-4{top:816px}

  /* title */
  .title-slide{background:var(--navy)}
  .brand-name{left:19px;top:31px;font-size:10px;font-weight:700}
  .brand-name span{font-weight:400}
  .signature-area{left:21px;top:80px;width:141px;height:14px;background:linear-gradient(90deg,rgba(255,255,255,.05),rgba(255,255,255,.25),rgba(255,255,255,.05))}
  .head-text{left:19px;top:140px;font-size:16.5px;font-weight:700;letter-spacing:-.2px}
  .title-slide .body-text{left:19px;top:166px;width:135px}

  /* agenda */
  .agenda-slide{background:var(--blue)}
  .agenda-title{left:7px;top:0;font-size:23px;font-weight:700}
  .agenda-rule{left:25px;top:4px;width:33px;height:1px;background:var(--white)}
  .agenda-card{top:57px;width:95px;height:127px;background:var(--navy);text-align:center}
  .agenda-card .num{margin-top:20px;font-size:16px;font-weight:700}
  .agenda-card .label{font-size:7px;font-weight:700;margin-top:1px}
  .agenda-card .body-text{margin:12px 12px 0}

  /* founder */
  .founder-slide{background:var(--sky)}
  .founder-title{left:36px;top:38px;font-size:18.5px;font-weight:800;line-height:1.05}
  .founder-rule{left:38px;top:99px;width:128px;height:1px;background:var(--white)}
  .founder-name{left:36px;top:117px;font-size:17px;font-weight:800;letter-spacing:.5px}
  .founder-role{left:38px;top:139px;font-size:6px;font-weight:700;letter-spacing:2.4px}
  .founder-slide .body-text{left:37px;top:166px;width:124px}
  .founder-photo{left:188px;top:17px;width:157px;height:201px;background:linear-gradient(160deg,#8fa3b8,#4f5d6c 60%,#2e3540)}

  /* vision */
  .vision-slide{background:var(--white)}
  .vision-panel{left:104px;top:16px;width:256px;height:202px;background:linear-gradient(135deg,var(--blue),var(--deep))}
  .vision-vertical{left:36px;top:206px;transform:rotate(-90deg);transform-origin:0 0;color:var(--navy);font-size:22px;font-weight:800;line-height:1.1;width:200px;white-space:nowrap}
  .vision-rule{left:28px;top:171px;width:2px;height:33px;background:var(--navy)}
  .icon-circle{width:34px;height:34px;border-radius:50%;background:var(--white)}
  .vision-head{font-size:12px;font-weight:700}
  .vision-slide .body-text{width:108px}

  /* case study */
  .case-slide{background:var(--white)}
  .case-bar{left:0;top:0;width:48px;height:113px;background:var(--blue)}
  .case-vertical{left:14px;top:100px;transform:rotate(-90deg);transform-origin:0 0;font-size:13px;font-weight:800;white-space:nowrap}
  .case-band{left:0;top:113px;width:360px;height:105px;background:var(--navy)}
  .case-note{left:0;top:122px;width:176px;height:96px;background:#f3f5f7}
  .case-note .body-text{color:#333;margin:14px 20px 0 28px}
  .case-head{left:197px;top:26px;color:var(--navy);font-size:7px;font-weight:800}
  .case-sub{left:199px;top:40px;color:var(--navy);font-size:6.5px}
  .case-slide .lead{left:199px;top:57px;width:128px;color:#555}
  .challenge-head{left:276px;top:140px;font-size:6.5px;font-weight:700}
  .case-slide .challenge{left:276px;top:155px;width:72px}

  /* team */
  .team-slide{background:var(--deep)}
  .team-top{left:0;top:0;width:360px;height:98px;background:var(--sky)}
  .team-title{left:28px;top:8px;font-size:14px;font-weight:700}
  .team-rule{left:100px;top:20px;width:73px;height:1px;background:var(--white)}
  .member{top:140px;width:70px;text-align:center}
  .member .name{font-size:6.8px}
  .member .pos{font-size:3.8px;font-weight:700;margin-bottom:7px}
  .member .body-text{text-align:center;padding:0 8px}

  /* goals */
  .goals-slide{background:linear-gradient(135deg,var(--blue),var(--deep))}
  .goals-side{left:0;top:0;width:153px;height:218px;background:var(--grey)}
  .goals-title{left:15px;top:3px;color:var(--navy);font-size:14px;font-weight:700}
  .goal{width:82px}
  .goal h4{font-size:5.5px;font-weight:700;margin-bottom:3px;line-height:1.1}
  .goal .body-text{font-size:3.4px}

  /* about */
  .about-slide{background:radial-gradient(circle at 60% 10%,var(--bright),var(--blue) 60%,var(--navy))}
  .about-head{left:161px;top:71px;font-size:8.5px;font-weight:700}
  .about-slide .body-text{left:161px;top:92px;width:152px;text-align:left;line-height:1.7}
  .about-title{left:40px;top:163px;font-size:17px;font-weight:800;line-height:.85}
  .about-rule{left:40px;top:195px;width:37px;height:1px;background:var(--white)}

  /* services */
  .services-slide{background:var(--sky)}
  .services-photo{left:197px;top:0;width:163px;height:218px}
  .services-panel{left:14px;top:39px;width:219px;height:149px;background:linear-gradient(135deg,var(--blue),var(--navy))}
  .service{width:84px}
  .service h4{font-size:5.5px;font-weight:700;margin-bottom:3px}
  .service .body-text{font-size:3.4px}
  .services-vertical{left:328px;top:206px;transform:rotate(-90deg);transform-origin:0 0;font-size:14px;font-weight:800;white-space:nowrap}
  .services-rule{left:351px;top:131px;width:1px;height:72px;background:var(--white)}

  /* share */
  .share-slide{background:var(--white)}
  .share-item{left:243px;width:80px}
  .share-item h4{font-size:7.5px;font-weight:700;margin-bottom:3px}
  .share-label{font-size:9.5px;font-weight:600;fill:var(--white);font-family:"Mulish",sans-serif}

  /* clients */
  .clients-slide{background:linear-gradient(135deg,var(--blue),var(--navy))}
  .clients-top{left:0;top:0;width:360px;height:49px;background:var(--white)}
  .clients-title{left:27px;top:10px;color:var(--navy);font-size:15.5px;font-weight:700}
  .client-mark{width:32px;height:32px}
  .client h4{font-size:12px;font-weight:700;line-height:1}
  .client .body-text{width:92px;margin-top:3px}

  /* thanks */
  .thanks-slide{background:linear-gradient(135deg,var(--navy),var(--deep))}
  .thanks-text{left:0;top:73px;width:360px;text-align:center;font-size:33px;font-weight:800;line-height:.9}
</style>
</head>
<body>

<!-- Title -->
<section class="slide title-slide col-1 row-1">
  <svg class="svg-fill" viewBox="0 0 360 218">
    <defs>
      <linearGradient id="titlePhoto" x1="0" y1="0" x2="1" y2="1">
        <stop offset="0" stop-color="#b5b5b5"/><stop offset=".5" stop-color="#8a8a8a"/><stop offset="1" stop-color="#4c4c4c"/>
      </linearGradient>
    </defs>
    <g role="img" aria-label="Photo of a lawyer in an office">
      <polygon points="226,0 360,0 360,218 169,218" fill="url(#titlePhoto)"/>
      <polygon points="193,150 222,218 169,218" fill="#dedede"/>
    </g>
    <line x1="226" y1="0" x2="169" y2="218" stroke="#fff" stroke-width="1.2"/>
  </svg>
  <div class="abs brand-name">Trovanek-<span>lawyers</span></div>
  <div class="abs signature-area" role="img" aria-label="Handwritten signature"></div>
  <div class="abs head-text">HEAD TEXT HERE</div>
  <p class="abs body-text">Lorem ipsum is simply dummy text of the printing and typesetting industry. Lorem ipsum has been the industry's standard dummy text ever since the 1500s.</p>
</section>

<!-- Agenda -->
<section class="slide agenda-slide col-2 row-1">
  <svg class="svg-fill" viewBox="0 0 360 218">
    <polygon points="0,56 360,184 360,218 0,218" fill="var(--grey)"/>
    <line x1="0" y1="56" x2="360" y2="184" stroke="var(--gold)" stroke-width="1"/>
  </svg>
  <div class="abs agenda-rule"></div>
  <div class="abs agenda-title">agenda</div>
  <div class="abs agenda-card" style="left:32px"><div class="num">1</div><div class="label">TEXT HERE</div><p class="body-text">Lorem ipsum is simply dummy text of the printing and typesetting industry. Lorem ipsum has been the industry's standard dummy text ever since the 1500s.</p></div>
  <div class="abs agenda-card" style="left:132px"><div class="num">2</div><div class="label">TEXT HERE</div><p class="body-text">Lorem ipsum is simply dummy text of the printing and typesetting industry. Lorem ipsum has been the industry's standard dummy text ever since the 1500s.</p></div>
  <div class="abs agenda-card" style="left:232px"><div class="num">3</div><div class="label">TEXT HERE</div><p class="body-text">Lorem ipsum is simply dummy text of the printing and typesetting industry. Lorem ipsum has been the industry's standard dummy text ever since the 1500s.</p></div>
</section>

<!-- Founder -->
<section class="slide founder-slide col-3 row-1">
  <svg class="svg-fill" viewBox="0 0 360 218">
    <polygon points="0,175 225,18 360,218 0,218" fill="var(--blue)" opacity=".75"/>
    <polygon points="60,218 225,18 360,218" fill="var(--navy)" opacity=".55"/>
  </svg>
  <div class="abs founder-photo" role="img" aria-label="Portrait photo of the company founder"></div>
  <div class="abs founder-title">founder of<br>the company</div>
  <div class="abs founder-rule"></div>
  <div class="abs founder-name">MARLA</div>
  <div class="abs founder-role">CEO</div>
  <p class="abs body-text">Lorem ipsum dolor sit amet, consectetuer adipiscing elit, sed diam nonummy nibh euismod tincidunt ut laoreet dolore magna aliquam erat volutpat. Ut</p>
</section>

<!-- Vision & mission -->
<section class="slide vision-slide col-1 row-2">
  <div class="abs vision-panel"></div>
  <svg class="svg-fill" viewBox="0 0 360 218">
    <polygon points="104,16 124,16 104,48" fill="#7fb6e6"/>
    <polygon points="104,48 124,16 124,40" fill="var(--blue)"/>
  </svg>
  <div class="abs vision-rule"></div>
  <div class="abs vision-vertical">our vision<br>and mission</div>

  <div class="abs icon-circle" style="left:142px;top:77px">
    <svg viewBox="0 0 34 34" width="34" height="34"><circle cx="17" cy="15" r="6" fill="none" stroke="var(--navy)" stroke-width="2"/><line x1="17" y1="21" x2="17" y2="27" stroke="var(--navy)" stroke-width="2"/></svg>
  </div>
  <div class="abs vision-head" style="left:190px;top:58px">vision</div>
  <p class="abs body-text" style="left:190px;top:76px">Lorem ipsum is simply dummy text of the printing and typesetting industry. Lorem ipsum has been the industry's standard dummy text ever since the 1500s.</p>

  <div class="abs icon-circle" style="left:142px;top:148px">
    <svg viewBox="0 0 34 34" width="34" height="34"><circle cx="17" cy="17" r="9" fill="none" stroke="var(--navy)" stroke-width="1.5"/><circle cx="17" cy="17" r="5" fill="none" stroke="var(--navy)" stroke-width="1.5"/><circle cx="17" cy="17" r="1.6" fill="var(--navy)"/><line x1="17" y1="17" x2="25" y2="9" stroke="var(--navy)" stroke-width="1.5"/></svg>
  </div>
  <div class="abs vision-head" style="left:187px;top:130px">mission</div>
  <p class="abs body-text" style="left:187px;top:148px">Lorem ipsum is simply dummy text of the printing and typesetting industry. Lorem ipsum has been the industry's standard dummy text ever since the 1500s.</p>
</section>

<!-- Case study -->
<section class="slide case-slide col-2 row-2">
  <div class="abs case-bar"></div>
  <div class="abs case-vertical">case study</div>
  <div class="abs photo" style="left:34px;top:19px;width:146px;height:87px" role="img" aria-label="Photo of a client meeting"></div>
  <div class="abs case-head">CLIENTS BACKGROUND</div>
  <div class="abs case-sub">solution &amp; bunefits</div>
  <p class="abs body-text lead">Lorem ipsum is simply dummy text of the printing and typesetting industry. Lorem ipsum has been the industry's standard dummy text ever since the 1500s.</p>
  <div class="abs case-band"></div>
  <div class="abs case-note"><p class="body-text">Lorem ipsum is simply dummy text of the printing and typesetting industry. Lorem ipsum has been the industry's standard dummy text ever since the 1500s, when an unknown printer took a galley of type and scrambled it to make a type specimen book. It has survived not only five centuries, but also the leap into electronic typesetting, remaining essentially unchanged. It was popularised in the 1960s with the release of sheets containing passages, and more recently with desktop publishing software including versions of Lorem Ipsum.</p></div>
  <div class="abs photo" style="left:166px;top:125px;width:101px;height:88px" role="img" aria-label="Photo of lawyers at work"></div>
  <div class="abs challenge-head">challenge</div>
  <p class="abs body-text challenge">Lorem ipsum is simply dummy text of the printing and typesetting industry. Lorem ipsum has been the industry's standard dummy text ever since the 1500s.</p>
</section>

<!-- Team -->
<section class="slide team-slide col-3 row-2">
  <div class="abs team-top"></div>
  <div class="abs team-title">our team</div>
  <div class="abs team-rule"></div>
  <svg class="svg-fill" viewBox="0 0 360 218">
    <defs>
      <linearGradient id="teamPhoto" x1="0" y1="0" x2="1" y2="1"><stop offset="0" stop-color="#d0d0d0"/><stop offset="1" stop-color="#555"/></linearGradient>
    </defs>
    <g>
      <polygon points="53,60 90,97 53,134 16,97" fill="none" stroke="var(--gold)" stroke-width=".6"/>
      <polyline points="24,104 53,133 82,104" fill="none" stroke="#fff" stroke-width="3"/>
      <polygon points="53,69 81,97 53,125 25,97" fill="url(#teamPhoto)" role="img" aria-label="Team member photo"/>
    </g>
    <g transform="translate(85 0)">
      <polygon points="53,60 90,97 53,134 16,97" fill="none" stroke="var(--gold)" stroke-width=".6"/>
      <polyline points="24,104 53,133 82,104" fill="none" stroke="#fff" stroke-width="3"/>
      <polygon points="53,69 81,97 53,125 25,97" fill="url(#teamPhoto)" role="img" aria-label="Team member photo"/>
    </g>
    <g transform="translate(169 0)">
      <polygon points="53,60 90,97 53,134 16,97" fill="none" stroke="var(--gold)" stroke-width=".6"/>
      <polyline points="24,104 53,133 82,104" fill="none" stroke="#fff" stroke-width="3"/>
      <polygon points="53,69 81,97 53,125 25,97" fill="url(#teamPhoto)" role="img" aria-label="Team member photo"/>
    </g>
    <g transform="translate(253 0)">
      <polygon points="53,60 90,97 53,134 16,97" fill="none" stroke="var(--gold)" stroke-width=".6"/>
      <polyline points="24,104 53,133 82,104" fill="none" stroke="#fff" stroke-width="3"/>
      <polygon points="53,69 81,97 53,125 25,97" fill="url(#teamPhoto)" role="img" aria-label="Team member photo"/>
    </g>
  </svg>
  <div class="abs member" style="left:18px"><div class="name">TEXT HERE</div><div class="pos">position</div><p class="body-text">Lorem ipsum is simply dummy text of the printing and typesetting industry, standard dummy text ever since the 1500s.</p></div>
  <div class="abs member" style="left:103px"><div class="name">TEXT HERE</div><div class="pos">position</div><p class="body-text">Lorem ipsum is simply dummy text of the printing and typesetting industry, standard dummy text ever since the 1500s.</p></div>
  <div class="abs member" style="left:187px"><div class="name">TEXT HERE</div><div class="pos">position</div><p class="body-text">Lorem ipsum is simply dummy text of the printing and typesetting industry, standard dummy text ever since the 1500s.</p></div>
  <div class="abs member" style="left:271px"><div class="name">TEXT HERE</div><div class="pos">position</div><p class="body-text">Lorem ipsum is simply dummy text of the printing and typesetting industry, standard dummy text ever since the 1500s.</p></div>
</section>

<!-- Goals -->
<section class="slide goals-slide col-1 row-3">
  <div class="abs goals-side"></div>
  <div class="abs goals-title">our goals</div>
  <svg class="svg-fill" viewBox="0 0 360 218">
    <defs><linearGradient id="bar" x1="0" x2="1"><stop offset="0" stop-color="#2a78c8"/><stop offset="1" stop-color="var(--navy)"/></linearGradient></defs>
    <g stroke="#1f5fa6" stroke-width=".5" fill="none">
      <rect x="18" y="62" width="122" height="98"/>
      <line x1="18" y1="82" x2="140" y2="82"/><line x1="18" y1="101" x2="140" y2="101"/><line x1="18" y1="121" x2="140" y2="121"/><line x1="18" y1="140" x2="140" y2="140"/>
      <line x1="38" y1="62" x2="38" y2="160"/><line x1="59" y1="62" x2="59" y2="160"/><line x1="79" y1="62" x2="79" y2="160"/><line x1="100" y1="62" x2="100" y2="160"/><line x1="120" y1="62" x2="120" y2="160"/>
    </g>
    <g fill="url(#bar)">
      <rect x="22" y="114" width="13" height="46"/><rect x="43" y="96" width="13" height="64"/><rect x="64" y="78" width="13" height="82"/><rect x="86" y="128" width="13" height="32"/><rect x="107" y="114" width="13" height="46"/>
    </g>
    <g fill="#1f5fa6" font-size="4" font-family="Mulish,sans-serif">
      <text x="12" y="162">0</text><text x="12" y="142">1</text><text x="12" y="123">2</text><text x="12" y="103">3</text><text x="12" y="84">4</text>
      <text x="27" y="166">A</text><text x="48" y="166">B</text><text x="69" y="166">C</text><text x="91" y="166">D</text><text x="112" y="166">E</text>
    </g>
  </svg>
  <div class="abs goal" style="left:165px;top:43px"><h4>a. business plan</h4><p class="body-text">Lorem ipsum is simply dummy text of the printing and typesetting industry, standard dummy text ever since the 1500s.</p></div>
  <div class="abs goal" style="left:165px;top:93px"><h4>b. business plan</h4><p class="body-text">Lorem ipsum is simply dummy text of the printing and typesetting industry, standard dummy text ever since the 1500s.</p></div>
  <div class="abs goal" style="left:165px;top:143px"><h4>c. operation of solution</h4><p class="body-text">Lorem ipsum is simply dummy text of the printing and typesetting industry, standard dummy text ever since the 1500s.</p></div>
  <div class="abs goal" style="left:265px;top:43px"><h4>d. programmer for<br>objectives</h4><p class="body-text">Lorem ipsum is simply dummy text of the printing and typesetting industry, standard dummy text ever since the 1500s.</p></div>
  <div class="abs goal" style="left:265px;top:108px"><h4>e. systems &amp; solutions</h4><p class="body-text">Lorem ipsum is simply dummy text of the printing and typesetting industry, standard dummy text ever since the 1500s.</p></div>
</section>

<!-- About -->
<section class="slide about-slide col-2 row-3">
  <svg class="svg-fill" viewBox="0 0 360 218">
    <defs><linearGradient id="aboutPhoto" x1="0" y1="0" x2="1" y2="1"><stop offset="0" stop-color="#9a9a9a"/><stop offset=".5" stop-color="#c9c9c9"/><stop offset="1" stop-color="#3a3a3a"/></linearGradient></defs>
    <polygon points="18,36 60,36 206,184 18,184" fill="url(#aboutPhoto)" role="img" aria-label="Photo of the law office"/>
    <polygon points="70,46 343,46 343,167 189,167" fill="var(--deep)"/>
    <line x1="54" y1="30" x2="210" y2="188" stroke="#fff" stroke-width=".8"/>
    <line x1="70" y1="46" x2="343" y2="46" stroke="#4a97d6" stroke-width=".5"/>
  </svg>
  <div class="abs about-head">we are professional company</div>
  <p class="abs body-text">Lorem ipsum is simply dummy text of the printing and typesetting industry. Lorem ipsum has been the industry's standard dummy text ever since the 1500s, when an unknown printer took a galley of type and scrambled it to make a type specimen book. It has survived not only five centuries.</p>
  <div class="abs about-title">about<br>us</div>
  <div class="abs about-rule"></div>
</section>

<!-- Services -->
<section class="slide services-slide col-3 row-3">
  <div class="abs photo services-photo" role="img" aria-label="Photo of a consultation at the office"></div>
  <div class="abs services-panel"></div>
  <div class="abs service" style="left:30px;top:56px"><h4>1. services</h4><p class="body-text">Lorem ipsum is simply dummy text of the printing and typesetting industry, standard dummy text ever since the 1500s.</p></div>
  <div class="abs service" style="left:30px;top:101px"><h4>2. services</h4><p class="body-text">Lorem ipsum is simply dummy text of the printing and typesetting industry, standard dummy text ever since the 1500s.</p></div>
  <div class="abs service" style="left:30px;top:142px"><h4>3. services</h4><p class="body-text">Lorem ipsum is simply dummy text of the printing and typesetting industry, standard dummy text ever since the 1500s.</p></div>
  <div class="abs service" style="left:136px;top:56px"><h4>4. services</h4><p class="body-text">Lorem ipsum is simply dummy text of the printing and typesetting industry, standard dummy text ever since the 1500s.</p></div>
  <div class="abs service" style="left:136px;top:101px"><h4>5. services</h4><p class="body-text">Lorem ipsum is simply dummy text of the printing and typesetting industry, standard dummy text ever since the 1500s.</p></div>
  <div class="abs service" style="left:136px;top:142px"><h4>6. services</h4><p class="body-text">Lorem ipsum is simply dummy text of the printing and typesetting industry, standard dummy text ever since the 1500s.</p></div>
  <div class="abs services-vertical">our services</div>
  <div class="abs services-rule"></div>
</section>

<!-- Share chart -->
<section class="slide share-slide col-1 row-4">
  <svg class="svg-fill" viewBox="0 0 360 218">
    <defs><radialGradient id="shareBg" cx=".7" cy=".4" r=".8"><stop offset="0" stop-color="var(--bright)"/><stop offset="1" stop-color="var(--navy)"/></radialGradient></defs>
    <polygon points="145,0 360,0 360,218 144,218 194,108" fill="url(#shareBg)"/>
    <polygon points="145,0 245,0 194,108" fill="var(--deep)" opacity=".8"/>
    <g transform="translate(96 98) scale(1.08 0.76)">
      <g fill="#1a5ba6">
        <g transform="translate(0 24)">
          <path transform="translate(2.1 -2.1)" d="M0,-50 A50,50 0 0 1 50,0 L9,0 A9,9 0 0 0 0,-9 Z"/>
          <path transform="translate(0 3)" d="M50,0 A50,50 0 0 1 -50,0 L-9,0 A9,9 0 0 0 9,0 Z"/>
          <path transform="translate(-2.7 -1.4)" d="M-50,0 A50,50 0 0 1 -29.4,-40.5 L-5.3,-7.3 A9,9 0 0 0 -9,0 Z"/>
          <path transform="translate(-0.9 -2.9)" d="M-29.4,-40.5 A50,50 0 0 1 0,-50 L0,-9 A9,9 0 0 0 -5.3,-7.3 Z"/>
        </g>
        <g transform="translate(0 12)">
          <path transform="translate(2.1 -2.1)" d="M0,-50 A50,50 0 0 1 50,0 L9,0 A9,9 0 0 0 0,-9 Z"/>
          <path transform="translate(0 3)" d="M50,0 A50,50 0 0 1 -50,0 L-9,0 A9,9 0 0 0 9,0 Z"/>
          <path transform="translate(-2.7 -1.4)" d="M-50,0 A50,50 0 0 1 -29.4,-40.5 L-5.3,-7.3 A9,9 0 0 0 -9,0 Z"/>
          <path transform="translate(-0.9 -2.9)" d="M-29.4,-40.5 A50,50 0 0 1 0,-50 L0,-9 A9,9 0 0 0 -5.3,-7.3 Z"/>
        </g>
      </g>
      <g fill="var(--cyan)" stroke="#7fcdf3" stroke-width=".6">
        <path transform="translate(2.1 -2.1)" d="M0,-50 A50,50 0 0 1 50,0 L9,0 A9,9 0 0 0 0,-9 Z"/>
        <path transform="translate(0 3)" d="M50,0 A50,50 0 0 1 -50,0 L-9,0 A9,9 0 0 0 9,0 Z"/>
        <path transform="translate(-2.7 -1.4)" d="M-50,0 A50,50 0 0 1 -29.4,-40.5 L-5.3,-7.3 A9,9 0 0 0 -9,0 Z"/>
        <path transform="translate(-0.9 -2.9)" d="M-29.4,-40.5 A50,50 0 0 1 0,-50 L0,-9 A9,9 0 0 0 -5.3,-7.3 Z"/>
      </g>
    </g>
    <text class="share-label" x="69" y="77">10%</text>
    <text class="share-label" x="107" y="86">25%</text>
    <text class="share-label" x="54" y="105">15%</text>
    <text class="share-label" x="98" y="130">50%</text>
  </svg>
  <div class="abs share-item" style="top:15px"><h4>10 %</h4><p class="body-text">Lorem ipsum is simply dummy text of the printing and typesetting industry, standard dummy text ever since the 1500s.</p></div>
  <div class="abs share-item" style="top:65px"><h4>15%</h4><p class="body-text">Lorem ipsum is simply dummy text of the printing and typesetting industry. Lorem ipsum has been the industry's standard dummy text ever</p></div>
  <div class="abs share-item" style="top:112px"><h4>25%</h4><p class="body-text">Lorem ipsum is simply dummy text of the printing and typesetting industry. Lorem ipsum has been the industry's standard dummy text ever</p></div>
  <div class="abs share-item" style="top:164px"><h4>50%</h4><p class="body-text">Lorem ipsum is simply dummy text of the printing and typesetting industry. Lorem ipsum has been the industry's standard dummy text ever</p></div>
</section>

<!-- Clients -->
<section class="slide clients-slide col-2 row-4">
  <div class="abs clients-top"></div>
  <div class="abs clients-title">our clients</div>
  <div class="abs client-mark" style="left:27px;top:86px;background:#e52a5b"></div>
  <div class="abs client" style="left:68px;top:72px"><h4>client 1</h4><p class="body-text">Lorem ipsum is simply dummy text of the printing and typesetting industry. Lorem ipsum has been the industry's standard dummy text ever since the 1500s.</p></div>
  <div class="abs client-mark" style="left:27px;top:149px;background:#f4b63c"></div>
  <div class="abs client" style="left:68px;top:135px"><h4>client 2</h4><p class="body-text">Lorem ipsum is simply dummy text of the printing and typesetting industry. Lorem ipsum has been the industry's standard dummy text ever since the 1500s.</p></div>
  <div class="abs client-mark" style="left:193px;top:86px;background:#28b0c8"></div>
  <div class="abs client" style="left:230px;top:72px"><h4>client 3</h4><p class="body-text">Lorem ipsum is simply dummy text of the printing and typesetting industry. Lorem ipsum has been the industry's standard dummy text ever since the 1500s.</p></div>
  <div class="abs client-mark" style="left:193px;top:149px;background:#3a4ba8"></div>
  <div class="abs client" style="left:230px;top:135px"><h4>client 4</h4><p class="body-text">Lorem ipsum is simply dummy text of the printing and typesetting industry. Lorem ipsum has been the industry's standard dummy text ever since the 1500s.</p></div>
</section>

<!-- Thank you -->
<section class="slide thanks-slide col-3 row-4">
  <div class="abs thanks-text">thank<br>you</div>
</section>

</body>
</html>
```